A Weather Forecasting Site needs designs

We need a website design for our new venture which is a weather forecasting website. This website should have the latest design trends.

Menu
Weather, Maps, Videos and Photos

The home page requirements are as follows:
- Search Bar
- Local Weather
- Weather forecast of major cities in the World
Favorite locations
- Space for ADs
- Email signup

Weather Details page
This page will be redirected from the home page when you click on any of the weather forecast section

We are open to all kinds of designs and ideas. Feel free to you colors which suite your design.

```html
<!DOCTYPE html>
<html lang="en">
<head>
<meta charset="utf-8">
<title>Skyvane — Weather Forecast</title>
<link rel="stylesheet" href="https://fonts.googleapis.com/css2?family=Roboto:wght@300;400;500&family=Roboto+Slab:wght@300;400&display=swap">
<style>
:root{
  --blue:#1a9ad6;
  --band:#109be0;
  --ink:#444;
  --line:#e3e5e8;
  --soft:#f5f6f8;
  --hero:#000;
  --footer:#2b2b2b;
  --btn:#5c5c5c;
  --sunny:#e8b52a;
  --cloudy:#8e9aa6;
}
*{margin:0;padding:0;box-sizing:border-box}
html,body{width:751px;height:1200px;overflow:hidden;background:#fff}
body{position:relative;font-family:"Roboto",sans-serif;color:var(--ink)}
.abs{position:absolute}

/* header */
.header{left:0;top:0;width:751px;height:54px;background:#fff}
.brand{left:53px;top:14px;font-family:"Roboto Slab",serif;font-size:21px;color:var(--blue);font-weight:400;line-height:26px}
.nav{left:185px;top:25px;display:flex;font-size:7px;letter-spacing:.3px;color:#555;font-weight:500;line-height:9px}
.nav span{margin-right:27px}
.nav .active{color:var(--blue)}
.nav-sep{left:550px;top:19px;width:1px;height:18px;background:#ccc}
.search{left:558px;top:18px;width:137px;height:21px;border:1px solid #d6d6d6;border-radius:3px;font-size:7px;color:#888;padding:6px 6px;line-height:8px}
.search svg{position:absolute;right:6px;top:6px}

/* hero */
.hero{left:0;top:54px;width:751px;height:355px;background:var(--hero);overflow:hidden}
.hero-photo{left:300px;top:0;width:451px;height:355px;background:linear-gradient(90deg,#000 0,#1b2230 35%,#4f6478 60%,#5b4236 100%)}
.local-title{left:57px;top:72px;font-family:"Roboto Slab",serif;font-weight:300;font-size:19px;color:#fff;line-height:24px}
.temp-now{left:54px;top:104px;font-size:58px;font-weight:500;color:#fff;letter-spacing:-1px;line-height:66px}
.temp-hi,.temp-lo{left:192px;font-size:19px;font-weight:300;color:#fff;line-height:22px}
.temp-hi{top:114px}.temp-lo{top:137px}
.days{left:56px;top:230px;display:flex}
.day{width:65px;height:66px;border-left:1.5px solid #ddd;text-align:center;color:#fff;font-size:17px;font-weight:300;padding-top:2px;line-height:20px}
.day:last-child{width:0}
.day-icon{display:block;margin:8px auto 0;width:40px;height:26px;border-radius:13px}
.sunny-cloud{background:var(--sunny)}
.sun{width:28px;border-radius:50%;background:var(--sunny)}
.rain-cloud{background:var(--cloudy)}

/* cities */
.cities{left:0;top:409px;width:751px;height:311px;background:var(--soft)}
.kicker{left:0;top:24px;width:751px;text-align:center;font-family:"Roboto Slab",serif;font-weight:300;font-size:11.5px;color:#555;line-height:14px}
.headline{left:0;top:42px;width:751px;text-align:center;font-family:"Roboto Slab",serif;font-weight:300;font-size:17px;color:var(--blue);line-height:22px}
.card{top:82px;width:155px;height:203px;background:#fff;border:1px solid var(--line)}
.card-art{left:28px;top:8px;width:99px;height:62px;border-radius:6px}
.art-rain{background:linear-gradient(#6f7378 0,#8d9196 50%,#fff 100%)}
.art-storm{background:linear-gradient(#6f7378 0,#8d9196 55%,#f2cc3a 100%)}
.art-sun{background:linear-gradient(110deg,#f0a850 0,#f7c06a 45%,#b9d3e4 60%,#fff 100%)}
.art-cloud{background:linear-gradient(#fff 0,#b9d3e4 35%,#b9d3e4 70%,#fff 100%)}
.card-date{left:0;top:78px;width:100%;text-align:center;font-size:10px;color:#555;line-height:12px}
.card-date sup{font-size:6px}
.card-status{left:0;top:100px;width:100%;text-align:center;font-size:9.5px;color:var(--blue);line-height:12px}
.card-rule{left:0;top:121px;width:100%;height:1px;background:var(--line)}
.card-row{left:22px;width:112px;display:flex;justify-content:space-between;font-size:8px;color:#666;line-height:10px}
.card-row b{font-weight:400}

/* favourites */
.fav-title{left:54px;top:741px;font-family:"Roboto Slab",serif;font-weight:300;font-size:12.5px;color:var(--blue);line-height:16px}
.fav-photo{top:765px;width:228px;height:114px}
.photo-rainbow{background:linear-gradient(#3a78c2 0,#4f8fd4 60%,#9bbbe4 100%)}
.photo-lightning{background:linear-gradient(#6a4e86 0,#3c2d58 60%,#1c1830 100%)}
.fav-name{top:889px;font-family:"Roboto Slab",serif;font-weight:300;font-size:12.5px;color:#555;line-height:16px}
.fav-text{top:914px;width:230px;font-size:7px;line-height:15.5px;color:#888}
.ad-slot{left:534px;top:750px;width:162px;height:219px;background:linear-gradient(#2a6fb0 0,#1f5b98 55%,#1b4f86 100%);border:1px solid #dcdcdc}

/* signup */
.signup{left:0;top:993px;width:751px;height:60px;background:var(--band)}
.signup-label{left:110px;top:17px;font-family:"Roboto Slab",serif;font-weight:300;font-size:18px;color:#fff;line-height:24px}
.signup-input{left:237px;top:18px;width:323px;height:24px;background:#fff;border-radius:2px;font-size:7px;color:#666;padding:0 13px;line-height:24px}
.signup-btn{left:565px;top:18px;width:92px;height:24px;background:var(--btn);color:#fff;font-family:"Roboto Slab",serif;font-size:10.5px;text-align:center;line-height:24px}

/* footer */
.footer{left:0;top:1053px;width:751px;height:147px;background:var(--footer)}
.social{top:20px;width:38px;height:38px;border:1px solid #8a8a8a;border-radius:50%}
.social svg{position:absolute;left:12px;top:13px}
.foot-rule{left:54px;top:67px;width:643px;height:1px;background:#3d3d3d}
.foot-nav{left:0;top:83px;width:751px;display:flex;justify-content:center;font-family:"Roboto Slab",serif;font-size:7.5px;color:#cfcfcf;line-height:10px}
.foot-nav span{padding:0 12px}
.foot-nav i{font-style:normal;color:#888}
.copyright{left:0;top:110px;width:751px;text-align:center;font-family:"Roboto Slab",serif;font-weight:300;font-size:7px;color:#cfcfcf;line-height:10px}
</style>
</head>
<body>

<header class="header abs">
  <div class="brand abs">Skyvane</div>
  <nav class="nav abs">
    <span class="active">HOME</span><span>WEATHER</span><span>MAPS</span><span>VIDEOS</span><span>PHOTOS</span><span>ABOUT</span><span>CONTACT</span>
  </nav>
  <div class="nav-sep abs"></div>
  <div class="search abs">Search
    <svg width="8" height="8" viewBox="0 0 8 8"><circle cx="3.3" cy="3.3" r="2.5" fill="none" stroke="#999" stroke-width="1"/><line x1="5.2" y1="5.2" x2="7.5" y2="7.5" stroke="#999" stroke-width="1"/></svg>
  </div>
</header>

<section class="hero abs">
  <div class="hero-photo abs" role="img" aria-label="Photo of a hand touching a cloud with the sun shining behind it"></div>
  <div class="local-title abs">Local Weather</div>
  <div class="temp-now abs">18°C</div>
  <div class="temp-hi abs">13°C</div>
  <div class="temp-lo abs">7°C</div>
  <div class="days abs">
    <div class="day">Mon<span class="day-icon sunny-cloud" role="img" aria-label="Sun behind cloud"></span></div>
    <div class="day">Tue<span class="day-icon sun" role="img" aria-label="Sunny"></span></div>
    <div class="day">Wed<span class="day-icon sunny-cloud" role="img" aria-label="Sun behind cloud"></span></div>
    <div class="day">Thu<span class="day-icon rain-cloud" role="img" aria-label="Rain cloud"></span></div>
    <div class="day">Fri<span class="day-icon sunny-cloud" role="img" aria-label="Sun behind cloud"></span></div>
    <div class="day">Sat<span class="day-icon rain-cloud" role="img" aria-label="Rain cloud"></span></div>
    <div class="day"></div>
  </div>
</section>

<section class="cities abs">
  <div class="kicker abs">WEATHER FORECAST OF</div>
  <div class="headline abs">MAJOR CITIES IN THE WORLD</div>

  <article class="card abs" style="left:54px">
    <div class="card-art abs art-rain" role="img" aria-label="Rain clouds illustration"></div>
    <div class="card-date abs">MON 5<sup>0</sup> / 41<sup>0</sup></div>
    <div class="card-status abs">SUNNY MILD</div>
    <div class="card-rule abs"></div>
    <div class="card-row abs" style="top:137px"><b>Wind Gust</b><b>:</b><b>44kmh</b></div>
    <div class="card-row abs" style="top:161px"><b>Rain</b><b>:</b><b>0mm</b></div>
    <div class="card-row abs" style="top:185px"><b>Snow</b><b>:</b><b>0mm</b></div>
  </article>

  <article class="card abs" style="left:217px">
    <div class="card-art abs art-storm" role="img" aria-label="Thunderstorm clouds illustration"></div>
    <div class="card-date abs">TUE 5<sup>0</sup> / 41<sup>0</sup></div>
    <div class="card-status abs">SUNNY MILD</div>
    <div class="card-rule abs"></div>
    <div class="card-row abs" style="top:137px"><b>Wind Gust</b><b>:</b><b>44kmh</b></div>
    <div class="card-row abs" style="top:161px"><b>Rain</b><b>:</b><b>0mm</b></div>
    <div class="card-row abs" style="top:185px"><b>Snow</b><b>:</b><b>0mm</b></div>
  </article>

  <article class="card abs" style="left:379px">
    <div class="card-art abs art-sun" role="img" aria-label="Sun and cloud illustration"></div>
    <div class="card-date abs">WED 5<sup>0</sup> / 41<sup>0</sup></div>
    <div class="card-status abs">LOW CLOUDS COOL</div>
    <div class="card-rule abs"></div>
    <div class="card-row abs" style="top:137px"><b>Wind Gust</b><b>:</b><b>44kmh</b></div>
    <div class="card-row abs" style="top:161px"><b>Rain</b><b>:</b><b>0mm</b></div>
    <div class="card-row abs" style="top:185px"><b>Snow</b><b>:</b><b>0mm</b></div>
  </article>

  <article class="card abs" style="left:542px">
    <div class="card-art abs art-cloud" role="img" aria-label="Two clouds illustration"></div>
    <div class="card-date abs">THR 5<sup>0</sup> / 41<sup>0</sup></div>
    <div class="card-status abs">MOSTLY CLOUDY COOL</div>
    <div class="card-rule abs"></div>
    <div class="card-row abs" style="top:137px"><b>Wind Gust</b><b>:</b><b>44kmh</b></div>
    <div class="card-row abs" style="top:161px"><b>Rain</b><b>:</b><b>0mm</b></div>
    <div class="card-row abs" style="top:185px"><b>Snow</b><b>:</b><b>0mm</b></div>
  </article>
</section>

<section>
  <div class="fav-title abs">FAVORITE LOCATIONS</div>
  <div class="fav-photo abs photo-rainbow" style="left:54px" role="img" aria-label="Photo of a bright sky with sun, clouds and a rainbow"></div>
  <div class="fav-photo abs photo-lightning" style="left:292px" role="img" aria-label="Photo of lightning over a city at night"></div>
  <div class="fav-name abs" style="left:54px">American</div>
  <div class="fav-name abs" style="left:292px">Singapore</div>
  <p class="fav-text abs" style="left:54px">Sed ut perspiciatis unde omnis iste natus error sit voluptatem accusantium doloremque laudantium, totam rem aperiam, eaque quasi architecto beatae vitae dicta sunt explicabo.</p>
  <p class="fav-text abs" style="left:292px">Sed ut perspiciatis unde omnis iste natus error sit voluptatem accusantium doloremque laudantium, totam rem aperiam, eaque quasi architecto beatae vitae dicta sunt explicabo.</p>
  <div class="ad-slot abs" role="img" aria-label="Advertisement space showing a weather app widget"></div>
</section>

<section class="signup abs">
  <div class="signup-label abs">Email Signup :</div>
  <div class="signup-input abs">Enter Your Email :</div>
  <div class="signup-btn abs">SUBMIT</div>
</section>

<footer class="footer abs">
  <div class="social abs" style="left:244px"></div>
  <div class="social abs" style="left:289px"></div>
  <div class="social abs" style="left:334px"></div>
  <div class="social abs" style="left:379px"></div>
  <div class="social abs" style="left:423px"></div>
  <div class="social abs" style="left:469px">
    <svg width="12" height="10" viewBox="0 0 12 10"><rect x=".5" y=".5" width="11" height="9" rx="1" fill="none" stroke="#fff" stroke-width="1"/><path d="M1 1l5 4 5-4" fill="none" stroke="#fff" stroke-width="1"/></svg>
  </div>
  <div class="foot-rule abs"></div>
  <div class="foot-nav abs">
    <span>HOME</span><i>|</i><span>WEATHER</span><i>|</i><span>MAPS</span><i>|</i><span>VIDEOS</span><i>|</i><span>PHOTOS</span><i>|</i><span>ABOUT</span><i>|</i><span>CONTACT</span>
  </div>
  <div class="copyright abs">© Copyrights 2017 Skyvane.All Rights Reserved.</div>
</footer>

</body>
</html>
```